New design and build for natural product Nasovera nosespray

We are looking for a new design for an existing website.

Nasovera is a natural product. we have three types of products. Please have a look at the existing site: nasovera-example.com

We are looking for a natural look and feel. This because the products are 100 procent natural.

We would like to have the following site structure (rows) :
- Picture of a person in nature
- Packshot
- Tekst
- 4 blocks for the four nasal issues with pictures
- Tekst
- 3 blocks with pictures to explain experiences from others.
- I think a need an extra white block with tekst (like this example ‘let your dreams come true’

Please have a look at the attached pdf.
page 2 is a idea where the site structure is important.
page 3 is an existing folder. Idear is to keep the folder look and feel in line with the new site design.
page 4-5-6 Element that are posible.
page 7 design that is too much.

Beside the home page I would like to have a template for the sales page.

The existing site has a large woocommerce customer database. This must stay available.
I have a staging site available where you can build the site. From here we can export and import the new disgn to the production site.

Please make the site in Divi

```html
<!DOCTYPE html>
<html lang="en">
<head>
<meta charset="utf-8">
<title>Nasovera – Breathe free through the nose again</title>
<link href="https://fonts.googleapis.com/css2?family=Montserrat:wght@700;800&family=Roboto:wght@400;500;700&display=swap" rel="stylesheet">
<style>
:root{
  --dark:#4a5157;
  --green:#6e7a62;
  --green-text:#4f7a3a;
  --red:#dc1f26;
  --band:#dc3e3e;
  --ink:#222;
  --muted:#6b6b6b;
  --soft:#f2f2f2;
  --white:#fff;
}
*{box-sizing:border-box;margin:0;padding:0}
html,body{width:1200px;height:3192px;overflow:hidden}
body{font-family:'Roboto',sans-serif;color:var(--ink);background:var(--white);position:relative}
a{color:inherit;text-decoration:none}
.abs{position:absolute}

/* top bar */
.topbar{position:absolute;top:0;left:0;width:1200px;height:46px;background:var(--dark);color:var(--white);font-size:13px;font-weight:500}
.topbar .left{left:110px;top:15px}
.topbar .mid{left:0;width:1240px;text-align:center;top:15px}
.topbar .tools{right:110px;top:12px;display:flex;gap:10px;align-items:center;font-size:14px}

/* header */
.header{position:absolute;top:46px;left:0;width:1200px;height:86px;background:var(--white)}
.brand{left:112px;top:14px;display:flex;align-items:center;gap:10px;font-family:'Montserrat',sans-serif;font-weight:800;font-size:30px;color:var(--dark)}
.brand .dot{width:26px;height:26px;border-radius:50%;background:var(--dark)}
.nav{left:342px;top:36px;display:flex;gap:29px;font-size:13.5px;font-weight:700;color:var(--ink)}
.btn-shop{left:965px;top:19px;width:123px;height:48px;background:var(--red);color:var(--white);font-weight:700;font-size:14.5px;display:flex;align-items:center;justify-content:center;border-radius:3px}

/* hero */
.hero{position:absolute;top:132px;left:0;width:1200px;height:600px;background:linear-gradient(100deg,#3f4a1d 0%,#7d7a2b 30%,#c9a94a 48%,#8b7a4a 62%,#5f6a6f 80%,#3d4a24 100%)}
.hero h1{position:absolute;left:110px;top:218px;font-family:'Montserrat',sans-serif;font-weight:800;font-size:44px;line-height:58px;color:var(--white);text-transform:uppercase}

/* packshot card */
.pack{position:absolute;left:111px;top:653px;width:978px;height:387px;background:var(--white);box-shadow:0 2px 10px rgba(0,0,0,.18)}
.pack .shot{left:95px;top:40px;width:220px;height:300px;background:linear-gradient(90deg,#d8252b 0 48%,#fff 48% 58%,#e8e2d2 58% 100%);border-radius:4px}
.pack ul{position:absolute;left:405px;top:70px;list-style:none;width:480px}
.pack li{position:relative;padding-left:55px;color:#666;font-size:22px;line-height:32px;margin-bottom:20px}
.pack li.dot::before{content:"";position:absolute;left:12px;top:12px;width:11px;height:11px;border-radius:50%;background:var(--band)}
.pack li.yes{color:var(--ink);font-size:25px;line-height:36px}
.pack li.yes svg{position:absolute;left:4px;top:6px}

/* complaints */
.complaints{position:absolute;top:1136px;left:0;width:1200px;height:500px;background:var(--green)}
.sec-title{font-family:'Montserrat',sans-serif;font-weight:700;text-transform:uppercase;text-align:center}
.complaints h2{position:absolute;top:63px;width:1200px;font-size:31px;color:var(--white)}
.ccard{position:absolute;top:138px;width:232px;height:292px;background:var(--white);border-radius:3px;text-align:center}
.ccard .img{position:absolute;left:6px;top:6px;width:220px;height:151px}
.ccard .heart{position:absolute;right:13px;top:16px;width:26px;height:26px;border-radius:50%;background:rgba(255,255,255,.35);display:flex;align-items:center;justify-content:center}
.ccard h3{position:absolute;top:167px;width:100%;font-size:19px;font-weight:500}
.ccard p{position:absolute;top:202px;left:8px;right:8px;font-size:13.5px;line-height:20px;color:var(--muted)}
.ccard .more{position:absolute;top:255px;width:100%;font-size:13.5px;font-weight:700;color:var(--green-text);display:flex;justify-content:center;align-items:center;gap:10px}

/* band */
.band{position:absolute;top:1636px;left:0;width:1200px;height:170px;background:var(--band);color:var(--white)}
.band h2{position:absolute;top:39px;width:1200px;font-size:35px}
.band p{position:absolute;top:100px;width:1200px;text-align:center;font-size:24px;font-weight:500}

/* experiences */
.ecard{position:absolute;top:1900px;width:313px;height:388px;background:var(--white);box-shadow:0 1px 6px rgba(0,0,0,.15);text-align:center}
.ecard .img{position:absolute;left:6px;top:7px;width:301px;height:197px}
.ecard .date{position:absolute;right:16px;top:37px;width:44px;height:44px;border-radius:50%;background:rgba(60,60,60,.7);color:var(--white);font-size:12px;font-weight:700;line-height:14px;display:flex;flex-direction:column;justify-content:center}
.ecard h3{position:absolute;top:216px;left:10px;right:10px;font-size:21px;line-height:26px;font-weight:500}
.ecard p{position:absolute;top:290px;left:10px;right:10px;font-size:14px;line-height:23px;color:var(--muted)}
.btn-read{position:absolute;top:2263px;width:128px;height:48px;background:var(--red);color:var(--white);font-size:14.5px;font-weight:500;display:flex;align-items:center;justify-content:center;border-radius:3px}

/* dreams */
.dreams{position:absolute;top:2408px;left:0;width:1200px;height:376px;background:var(--soft)}
.dreams h2{position:absolute;top:48px;left:0;width:1200px;font-size:34px;color:var(--green)}
.dreams .copy{position:absolute;left:110px;top:118px;width:725px;font-size:15px;line-height:26px;color:#7a7a7a;text-align:justify}
.dreams .copy p+p{margin-top:20px}
.dreams .leaf{position:absolute;left:890px;top:57px;width:200px;height:245px;background:radial-gradient(ellipse at center,#7d8a70 0%,#9aa590 50%,rgba(242,242,242,0) 72%)}

/* footer */
.footer{position:absolute;top:2784px;left:0;width:1200px;height:408px;background:var(--dark);color:var(--white)}
.footer h4{position:absolute;top:68px;font-size:17px;font-weight:700;text-transform:uppercase}
.footer ul{position:absolute;top:110px;list-style:none;font-size:14px;line-height:24px}
.footer li{position:relative;padding-left:33px}
.footer li svg{position:absolute;left:0;top:6px}
.footer .contact li{margin-bottom:9px}
.field{position:absolute;left:829px;width:260px;height:46px;background:var(--white);border-radius:3px;color:#444;font-size:14px;font-weight:500;padding:15px 12px}
.btn-sub{position:absolute;left:829px;top:271px;width:260px;height:46px;background:var(--red);border-radius:3px;font-size:15px;font-weight:700;display:flex;align-items:center;justify-content:center}
.footer .rule{position:absolute;left:110px;top:349px;width:979px;height:1px;background:rgba(255,255,255,.45)}
.footer .copy{position:absolute;top:371px;width:1200px;text-align:center;font-size:13.5px}
</style>
</head>
<body>

<div class="topbar">
  <div class="abs left">Verzendkosten 2,95 euro in NL</div>
  <div class="abs mid">Free Shipping with 3 or more</div>
  <div class="abs tools">
    <svg width="15" height="15" viewBox="0 0 16 16"><circle cx="6.5" cy="6.5" r="5" fill="none" stroke="#fff" stroke-width="2"/><path d="M10.5 10.5L15 15" stroke="#fff" stroke-width="2.2"/></svg>
    <svg width="16" height="16" viewBox="0 0 16 16"><circle cx="8" cy="8" r="7" fill="none" stroke="#fff" stroke-width="1.6"/><circle cx="8" cy="6.3" r="2.5" fill="#fff"/><path d="M3.5 13c1-2.5 8-2.5 9 0" fill="#fff"/></svg>
    <span style="display:flex;align-items:center;gap:2px"><svg width="17" height="15" viewBox="0 0 17 15"><path d="M0 1h3l2.5 9h9l2-6.5H4.5" fill="none" stroke="#fff" stroke-width="1.8"/><circle cx="6.5" cy="13" r="1.4" fill="#fff"/><circle cx="13" cy="13" r="1.4" fill="#fff"/></svg>(0)</span>
  </div>
</div>

<header class="header">
  <div class="abs brand"><span class="dot"></span>Nasovera</div>
  <nav class="abs nav"><a>HOME</a><a>PRODUCT</a><a>RESEARCH</a><a>EXPERIENCES</a><a>TIPS/INFO</a><a>CONTACT</a></nav>
  <a class="abs btn-shop">SHOP NOW</a>
</header>

<section class="hero" role="img" aria-label="Photo of a smiling woman breathing freely in a sunlit park">
  <h1>Breathe free through<br>the nose again</h1>
</section>

<section class="pack">
  <div class="abs shot" role="img" aria-label="Packshot of the Nasovera nasal spray box and bottle"></div>
  <ul>
    <li class="dot">Do you suffer from Runny or Chronic Nose Nasal Complaints?</li>
    <li class="dot">Can't Get Rid of Your Nasal Spray Addiction?</li>
    <li class="yes"><svg width="24" height="20" viewBox="0 0 24 20"><path d="M2 10l7 7L22 3" fill="none" stroke="#3f9a3a" stroke-width="4"/></svg>Try Nasovera Nasal Spray, The No 1. Natural Nasal Spray Based on Red Pepper</li>
  </ul>
</section>

<section class="complaints">
  <h2 class="sec-title">Chronic Nose Complaints</h2>
  <article class="ccard" style="left:111px">
    <div class="img" role="img" aria-label="Photo of a woman blowing her nose into a tissue" style="background:linear-gradient(135deg,#9aa3b5,#e8e2dc)"></div>
    <span class="heart"><svg width="14" height="13" viewBox="0 0 14 13"><path d="M7 12S1 8 1 4.2A3 3 0 0 1 7 3a3 3 0 0 1 6 1.2C13 8 7 12 7 12z" fill="none" stroke="#fff" stroke-width="1.4"/></svg></span>
    <h3>Stuffy Nose</h3>
    <p>A stuffy nose is usually caused by a cold.</p>
    <a class="more">KNOW MORE <svg width="12" height="12" viewBox="0 0 12 12"><circle cx="6" cy="6" r="5" fill="none" stroke="#4f7a3a" stroke-width="1.5"/><path d="M3.5 6h5M6.5 4l2 2-2 2" fill="none" stroke="#4f7a3a" stroke-width="1.5"/></svg></a>
  </article>
  <article class="ccard" style="left:360px">
    <div class="img" role="img" aria-label="Illustration of viruses and bacteria" style="background:linear-gradient(135deg,#4f9f93,#8cc7b8)"></div>
    <span class="heart"><svg width="14" height="13" viewBox="0 0 14 13"><path d="M7 12S1 8 1 4.2A3 3 0 0 1 7 3a3 3 0 0 1 6 1.2C13 8 7 12 7 12z" fill="none" stroke="#fff" stroke-width="1.4"/></svg></span>
    <h3>Running Nose</h3>
    <p>When the nose produces too much mucus, extra fluid</p>
    <a class="more">KNOW MORE <svg width="12" height="12" viewBox="0 0 12 12"><circle cx="6" cy="6" r="5" fill="none" stroke="#4f7a3a" stroke-width="1.5"/><path d="M3.5 6h5M6.5 4l2 2-2 2" fill="none" stroke="#4f7a3a" stroke-width="1.5"/></svg></a>
  </article>
  <article class="ccard" style="left:608px">
    <div class="img" role="img" aria-label="Photo of a man at a desk pinching the bridge of his nose" style="background:linear-gradient(135deg,#d9dcdf,#6f7780)"></div>
    <span class="heart"><svg width="14" height="13" viewBox="0 0 14 13"><path d="M7 12S1 8 1 4.2A3 3 0 0 1 7 3a3 3 0 0 1 6 1.2C13 8 7 12 7 12z" fill="none" stroke="#fff" stroke-width="1.4"/></svg></span>
    <h3>Sinusitis</h3>
    <p>Sinusitis is mainly caused by a cold.</p>
    <a class="more">KNOW MORE <svg width="12" height="12" viewBox="0 0 12 12"><circle cx="6" cy="6" r="5" fill="none" stroke="#4f7a3a" stroke-width="1.5"/><path d="M3.5 6h5M6.5 4l2 2-2 2" fill="none" stroke="#4f7a3a" stroke-width="1.5"/></svg></a>
  </article>
  <article class="ccard" style="left:857px">
    <div class="img" role="img" aria-label="Photo of a woman using a nasal spray" style="background:linear-gradient(135deg,#f1ece8,#b98f7a)"></div>
    <span class="heart"><svg width="14" height="13" viewBox="0 0 14 13"><path d="M7 12S1 8 1 4.2A3 3 0 0 1 7 3a3 3 0 0 1 6 1.2C13 8 7 12 7 12z" fill="none" stroke="#fff" stroke-width="1.4"/></svg></span>
    <h3>Nasal Spray Addiction</h3>
    <p>Most (non-natural) nasal sprays can only be used for a week.</p>
    <a class="more">KNOW MORE <svg width="12" height="12" viewBox="0 0 12 12"><circle cx="6" cy="6" r="5" fill="none" stroke="#4f7a3a" stroke-width="1.5"/><path d="M3.5 6h5M6.5 4l2 2-2 2" fill="none" stroke="#4f7a3a" stroke-width="1.5"/></svg></a>
  </article>
</section>

<section class="band">
  <h2 class="sec-title">Do you want more about</h2>
  <p>EXPERIENCES OF OTHERS?</p>
</section>

<article class="ecard" style="left:111px">
  <div class="img" role="img" aria-label="Photo of a man on a park bench holding his head" style="background:linear-gradient(160deg,#9fb27a,#c9c2b2 55%,#7a6a55)"></div>
  <div class="date"><span>19</span><span>Dec</span></div>
  <h3>Headache due to stuffy nose</h3>
  <p>Jeroen: For years I have suffered from a stuffy nose and persistent headaches because I [...]</p>
</article>
<article class="ecard" style="left:443px">
  <div class="img" role="img" aria-label="Photo of a relieved smiling woman with hands on her chest" style="background:linear-gradient(160deg,#8c8a86,#e6c8bd 55%,#c79d8c)"></div>
  <div class="date"><span>02</span><span>Feb</span></div>
  <h3>Sneezing, my nose reacts to everything. Nasovera helped</h3>
  <p>Sneezing Lotte: I have a chronic (idiopathic) cold. When a man with strong aftershave passes [...]</p>
</article>
<article class="ecard" style="left:775px">
  <div class="img" role="img" aria-label="Photo of a woman on a sofa sneezing into a tissue" style="background:linear-gradient(160deg,#e4e4e2,#b9b3aa 55%,#6a7f8f)"></div>
  <div class="date"><span>20</span><span>Aug</span></div>
  <h3>Cold due to air conditioning</h3>
  <p>Do you catch a cold in the summer? Could you catch a cold from the air conditioning? What have we [...]</p>
</article>
<a class="btn-read" style="left:204px">READ MORE</a>
<a class="btn-read" style="left:537px">READ MORE</a>
<a class="btn-read" style="left:869px">READ MORE</a>

<section class="dreams">
  <h2 class="sec-title">Let your dreams come true</h2>
  <div class="copy">
    <p>Lorem ipsum dolor sit amet, consectetur adipiscing elit, sed do eiusmod tempor incididunt ut labore et dolore magna aliqua. Ut enim ad minim veniam, quis nostrud exercitation ullamco laboris nisi ut aliquip ex ea commodo consequat. Duis aute irure dolor in reprehenderit in vim ad minim veniam, quis nostrud exercitoluptate velit esse cillum dolore eu fugiat nulla pariatur.</p>
    <p>Sed ut perspiciatis unde omnis iste natus error sit voluptatem accusantium doloremque laudantium, totam rem aperiam, eaque ipsa quae ab illo inventore veritatis im ad minim veniam, quis nostrud exercitet quasi architecto beatae vitae dicta sunt explicabo.</p>
  </div>
  <div class="leaf" role="img" aria-label="Illustration of a green palm leaf"></div>
</section>

<footer class="footer">
  <h4 style="left:110px">Information</h4>
  <ul style="left:110px">
    <li><svg width="13" height="13" viewBox="0 0 12 12"><circle cx="6" cy="6" r="5" fill="none" stroke="#dc3e3e" stroke-width="1.5"/><path d="M3.5 6h5M6.5 4l2 2-2 2" fill="none" stroke="#dc3e3e" stroke-width="1.5"/></svg>Privacy declaration</li>
    <li><svg width="13" height="13" viewBox="0 0 12 12"><circle cx="6" cy="6" r="5" fill="none" stroke="#dc3e3e" stroke-width="1.5"/><path d="M3.5 6h5M6.5 4l2 2-2 2" fill="none" stroke="#dc3e3e" stroke-width="1.5"/></svg>Terms and Conditions Nasovera</li>
    <li><svg width="13" height="13" viewBox="0 0 12 12"><circle cx="6" cy="6" r="5" fill="none" stroke="#dc3e3e" stroke-width="1.5"/><path d="M3.5 6h5M6.5 4l2 2-2 2" fill="none" stroke="#dc3e3e" stroke-width="1.5"/></svg>Pregnancy</li>
    <li><svg width="13" height="13" viewBox="0 0 12 12"><circle cx="6" cy="6" r="5" fill="none" stroke="#dc3e3e" stroke-width="1.5"/><path d="M3.5 6h5M6.5 4l2 2-2 2" fill="none" stroke="#dc3e3e" stroke-width="1.5"/></svg>Instructions for use Nasovera<br>nasal spray</li>
  </ul>

  <h4 style="left:393px">Our Service</h4>
  <ul style="left:393px">
    <li><svg width="13" height="13" viewBox="0 0 12 12"><circle cx="6" cy="6" r="5" fill="none" stroke="#dc3e3e" stroke-width="1.5"/><path d="M3.5 6h5M6.5 4l2 2-2 2" fill="none" stroke="#dc3e3e" stroke-width="1.5"/></svg>Contact</li>
    <li><svg width="13" height="13" viewBox="0 0 12 12"><circle cx="6" cy="6" r="5" fill="none" stroke="#dc3e3e" stroke-width="1.5"/><path d="M3.5 6h5M6.5 4l2 2-2 2" fill="none" stroke="#dc3e3e" stroke-width="1.5"/></svg>Shop</li>
    <li><svg width="13" height="13" viewBox="0 0 12 12"><circle cx="6" cy="6" r="5" fill="none" stroke="#dc3e3e" stroke-width="1.5"/><path d="M3.5 6h5M6.5 4l2 2-2 2" fill="none" stroke="#dc3e3e" stroke-width="1.5"/></svg>Send order</li>
    <li><svg width="13" height="13" viewBox="0 0 12 12"><circle cx="6" cy="6" r="5" fill="none" stroke="#dc3e3e" stroke-width="1.5"/><path d="M3.5 6h5M6.5 4l2 2-2 2" fill="none" stroke="#dc3e3e" stroke-width="1.5"/></svg>Stores</li>
    <li><svg width="13" height="13" viewBox="0 0 12 12"><circle cx="6" cy="6" r="5" fill="none" stroke="#dc3e3e" stroke-width="1.5"/><path d="M3.5 6h5M6.5 4l2 2-2 2" fill="none" stroke="#dc3e3e" stroke-width="1.5"/></svg>FAQ</li>
  </ul>

  <h4 style="left:562px">Contact</h4>
  <ul class="contact" style="left:562px">
    <li><svg width="11" height="14" viewBox="0 0 11 14"><path d="M5.5 13S1 8 1 5a4.5 4.5 0 0 1 9 0c0 3-4.5 8-4.5 8z" fill="#dc3e3e"/><circle cx="5.5" cy="5" r="1.6" fill="#4a5157"/></svg>Verdanta BV, Lindelaan<br>12, 3700 AB Zeist</li>
    <li><svg width="13" height="13" viewBox="0 0 13 13"><path d="M2 1l3 .5 1 3-1.6 1.2a7 7 0 0 0 3.4 3.4L9 7.5l3 1 .5 3-1.5 1C6 12.5.5 7 1 2z" fill="#dc3e3e"/></svg>+31 (0)30 -000 01 23</li>
    <li><svg width="14" height="11" viewBox="0 0 14 11"><rect x="0" y="0" width="14" height="11" rx="1" fill="#dc3e3e"/><path d="M0 1l7 5 7-5" fill="none" stroke="#4a5157" stroke-width="1.2"/></svg>info@nasovera-example.com</li>
    <li style="margin-top:8px;margin-bottom:2px"><svg width="13" height="13" viewBox="0 0 12 12"><circle cx="6" cy="6" r="5" fill="none" stroke="#dc3e3e" stroke-width="1.5"/><path d="M3.5 6h5M6.5 4l2 2-2 2" fill="none" stroke="#dc3e3e" stroke-width="1.5"/></svg>KvK: 00000000</li>
    <li><svg width="13" height="13" viewBox="0 0 12 12"><circle cx="6" cy="6" r="5" fill="none" stroke="#dc3e3e" stroke-width="1.5"/><path d="M3.5 6h5M6.5 4l2 2-2 2" fill="none" stroke="#dc3e3e" stroke-width="1.5"/></svg>BTW No: NL000.000.000B.01</li>
  </ul>

  <h4 style="left:829px">Newsletter</h4>
  <div class="field" style="top:112px">Email Address</div>
  <div class="field" style="top:165px">First Name</div>
  <div class="field" style="top:218px">Last Name</div>
  <a class="btn-sub">SUBSCRIBE</a>

  <div class="rule"></div>
  <div class="copy">© 2021 Company Name. All Rights Reserved</div>
</footer>

</body>
</html>
```